The Wellness Barn Business Card

Info for the front..... (in whichever order and layout looks best)
Carla Penhallow
Physiotherapist
4/37 Upper Creekbank Rd
Tallowbrook
QLD 4712
0462305178
carlapenhallow57@mailbox.example
www.thewellnessbarn.example.au
on the back I would like to be able to write appointments so probably just that heading with lines.
I like a sort of rustic style but mostly professional, colours in naturals, beige, brown, green etc. I dont mind if the logo colour is changed slightly to suit.

```html
<!DOCTYPE html>
<html lang="en">
<head>
<meta charset="utf-8">
<title>The Wellness Barn – Business Card</title>
<link href="https://fonts.googleapis.com/css2?family=Quicksand:wght@500;700&family=Dancing+Script:wght@400&display=swap" rel="stylesheet">
<style>
  :root {
    --page-bg: #e6e4df;
    --pattern-light: #d3dbb2;
    --pattern-mid: #bfcb94;
    --pattern-dark: #aebb7e;
    --band: #ffffff;
    --brand-green: #2c4a1e;
    --text-brown: #4b3d24;
    --rule: #3d5a2a;
    --dots: #5a4a2c;
  }
  * { box-sizing: border-box; margin: 0; padding: 0; }
  html, body { width: 1200px; height: 900px; overflow: hidden; }
  body {
    background: var(--page-bg);
    font-family: "Quicksand", sans-serif;
    color: var(--text-brown);
    display: flex;
    flex-direction: column;
    align-items: center;
    justify-content: center;
    gap: 56px;
  }
  .card {
    position: relative;
    width: 640px;
    height: 366px;
    border-radius: 4px;
    overflow: hidden;
    box-shadow: 0 10px 28px rgba(0,0,0,0.18);
  }
  .card-pattern {
    position: absolute;
    inset: 0;
    background: linear-gradient(135deg, var(--pattern-light) 0%, var(--pattern-mid) 55%, var(--pattern-dark) 100%);
  }
  .brand-name {
    position: absolute;
    font-family: "Quicksand", sans-serif;
    font-weight: 700;
    color: var(--brand-green);
    display: flex;
    align-items: center;
    gap: 12px;
    white-space: nowrap;
  }
  .brand-dot {
    width: 18px; height: 18px;
    border-radius: 50%;
    background: var(--brand-green);
  }

  /* Appointment side */
  .appointment .brand-name { top: 58px; left: 0; right: 0; justify-content: center; font-size: 38px; }
  .appointment-band {
    position: absolute;
    left: 0; right: 0; bottom: 0;
    height: 204px;
    background: var(--band);
  }
  .appointment-title {
    position: absolute;
    top: 28px; left: 0; right: 0;
    text-align: center;
    font-family: "Dancing Script", cursive;
    font-size: 34px;
    color: var(--brand-green);
  }
  .appointment-fields {
    position: absolute;
    left: 44px; right: 44px; top: 112px;
    display: flex;
    gap: 18px;
    font-size: 17px;
    font-weight: 500;
  }
  .field { display: flex; align-items: flex-end; gap: 8px; }
  .field-date { flex: 1.15; }
  .field-time { flex: 1; }
  .field-line { flex: 1; border-bottom: 2px dotted var(--dots); height: 16px; }

  /* Contact side */
  .contact .brand-name { top: 92px; right: 48px; font-size: 34px; }
  .contact-rule {
    position: absolute;
    left: 40px; right: 40px; top: 196px;
    border-top: 1.5px solid var(--rule);
  }
  .person {
    position: absolute;
    left: 44px; top: 206px;
  }
  .person-name {
    font-family: "Dancing Script", cursive;
    font-size: 31px;
    color: var(--brand-green);
    line-height: 1.1;
  }
  .person-role { font-size: 16px; font-weight: 500; margin-top: 2px; }
  .person-rule { width: 270px; border-top: 1.5px solid var(--rule); margin: 10px 0 8px; }
  .contact-list { list-style: none; font-size: 15px; font-weight: 500; line-height: 1.75; }
  .contact-list li { display: flex; align-items: center; gap: 8px; }
  .contact-list svg { width: 15px; height: 15px; flex: none; }
  .address {
    position: absolute;
    right: 44px; top: 208px;
    text-align: right;
    font-size: 16px;
    font-weight: 500;
    line-height: 1.45;
  }
</style>
</head>
<body>

  <section class="card appointment">
    <div class="card-pattern" role="img" aria-label="Soft olive green geometric triangle pattern background"></div>
    <div class="brand-name"><span class="brand-dot"></span>The Wellness Barn</div>
    <div class="appointment-band">
      <h2 class="appointment-title">Your Appointment</h2>
      <div class="appointment-fields">
        <div class="field field-date"><span>Date</span><span class="field-line"></span></div>
        <div class="field field-time"><span>Time</span><span class="field-line"></span></div>
      </div>
    </div>
  </section>

  <section class="card contact">
    <div class="card-pattern" role="img" aria-label="Soft olive green geometric triangle pattern background"></div>
    <div class="brand-name"><span class="brand-dot"></span>The Wellness Barn</div>
    <div class="contact-rule"></div>
    <div class="person">
      <div class="person-name">Carla Penhallow</div>
      <div class="person-role">Physiotherapist</div>
      <div class="person-rule"></div>
      <ul class="contact-list">
        <li>
          <svg viewBox="0 0 16 16" aria-hidden="true"><path fill="#2c4a1e" d="M3.6 1.2l2.3 2.6-1.2 1.8c.8 1.9 2.2 3.3 4.1 4.1l1.8-1.2 2.6 2.3-1.2 2.2c-5.5-.3-10-4.8-10.3-10.3z"/></svg>
          0462305178
        </li>
        <li>
          <svg viewBox="0 0 16 16" aria-hidden="true"><rect x="1" y="3" width="14" height="10" fill="#2c4a1e"/><path d="M1.5 3.5l6.5 5 6.5-5" stroke="#d3dbb2" stroke-width="1.2" fill="none"/></svg>
          carlapenhallow57@mailbox.example
        </li>
        <li>
          <svg viewBox="0 0 16 16" aria-hidden="true"><g fill="none" stroke="#2c4a1e" stroke-width="1.3"><circle cx="8" cy="8" r="6.5"/><ellipse cx="8" cy="8" rx="2.8" ry="6.5"/><path d="M1.5 8h13M2.5 4.8h11M2.5 11.2h11"/></g></svg>
          www.thewellnessbarn.example.au
        </li>
      </ul>
    </div>
    <address class="address" style="font-style:normal">
      4/37 Upper Creekbank Rd<br>
      Tallowbrook, QLD 4712
    </address>
  </section>

</body>
</html>
```